Cabling Business Graphic Design for Website

Hi,

We need a three pages designed for a cabling website: http://www.wirovant.com.au/

1.) Homepage
2.) Category Page
3.) Product Page

Wirovant is an online wholesaler of Server Racks and Cables.

Wirovant began in 2006 as an offshoot of a cabling installation company called Pyrosmel which has been around since 1993. Through Pyrosmel and the industry insight that gave use we saw the need for a direct, online wholesaler.

The problem we found the with the industry is the middle man. It seemed that industry suppliers were so obsessed with carving out distribution channels and establishing exclusive resellers and wholesalers that they began to alienate their products and price themselves out of the market.

Then came Wirovant - the first direct online data comms wholesaler to hit the industry.

We manufacture, import and sell direct - we have no middle men, keep our prices fair and our product range fresh.

Top three competitors:
Orbison Quarry - www.dulmep.com.au
Shelvantix - www.shelvantix.com.au
Brimtoll Messaging - www.brimtoll.net.au

Our range - we offer a massive range of products - we are always adding new and unique products.

Our Service - we have technical sales staff who are able to help with technical questions and provide advice on how to do things / what to buy - its not just a call centre situation.

We are able to custom manufacture cables and cabinets to suit specifications.

Its very easy to order from us, our turnaround time is 99% of the time 24 hours.

Please refer to the design brief file and the business uncovery for more information. The design brief files are quite specific so please ensure the design adheres to this brief.

Target Market(s)

IT Managers, Electricians, Network Integrators and IT companies.

They have a contract with schools and government departments to order their supplies. This is a massive section of their market.

Industry/Entity Type

Industry

Requirements
Must have
• Reinforce
* that the products adhere to government and industry certifications
* warranty / quality guarantee
* delivery details / stock availability
Nice to have
• Included in the Business Uncovery file
Should not have
• Included in the Business Uncovery

```html
<!DOCTYPE html>
<html lang="en">
<head>
<meta charset="utf-8">
<title>Wirovant — Wholesale Server Racks and Cables</title>
<link rel="stylesheet" href="https://fonts.googleapis.com/css2?family=Arimo:wght@400;700&family=Tinos:ital@1&display=swap">
<style>
:root{
  --page:#151515;
  --ink:#333;
  --muted:#666;
  --red:#c8100f;
  --red-dark:#8e0c0b;
  --white:#fff;
  --line:#d9d9d9;
  --panel:#f4f4f4;
  --footer:#2b2b2b;
  --foot-text:#d6d6d6;
}
*{box-sizing:border-box;margin:0;padding:0}
html,body{width:874px;height:1200px;overflow:hidden}
body{background:var(--page);font-family:"Arimo",Arial,sans-serif;color:var(--ink);position:relative}
.abs{position:absolute}
.top-rule{left:0;top:0;width:874px;height:4px;background:var(--red)}

/* header */
.brand{left:57px;top:40px;color:var(--white);font-weight:700;font-size:34px;letter-spacing:-1px;display:flex;align-items:center;gap:10px}
.brand .mark{width:18px;height:18px;background:var(--red)}
.search{left:248px;top:50px;width:421px;height:49px;background:#e9e9e9;border-radius:3px;padding:10px 8px;display:flex;gap:6px}
.search .field{flex:1;background:var(--white);border:1px solid #bbb;border-radius:4px;font-size:11px;color:#888;padding:8px 10px}
.search .go{width:80px;background:linear-gradient(#e0201e,#b20c0b);color:var(--white);font-weight:700;font-size:14px;border-radius:5px;display:flex;align-items:center;justify-content:center}
.support-avatar{left:694px;top:32px;width:32px;height:32px;background:linear-gradient(#c9c9c9,#7a2222);border-radius:4px}
.support{left:743px;top:34px;color:#ddd;font-size:11px;line-height:15px}
.phone{left:706px;top:72px;color:var(--white);font-size:16px;display:flex;align-items:center;gap:22px}
.hours{left:700px;top:98px;color:#ddd;font-size:10px}

/* main sheet */
.sheet{left:32px;top:119px;width:810px;height:872px;background:var(--white)}
.nav{left:40px;top:126px;width:794px;height:29px;background:linear-gradient(#d81614,#a50b0a);display:flex;align-items:center;padding-left:10px;gap:8px;font-size:10.6px;color:var(--white);white-space:nowrap}
.nav .login{margin-left:auto;background:#e01512;color:#111;height:100%;display:flex;align-items:center;padding:0 8px}

/* left column */
.cats{left:40px;top:166px;width:159px;height:321px;border:1px solid var(--line);background:var(--white)}
.cats li{list-style:none;height:24px;border-bottom:1px solid #e6e6e6;font-size:11px;font-weight:700;color:#333;padding:5px 8px;display:flex;justify-content:space-between}
.cats li .arr{color:#17406e}
.promo{left:40px;width:159px;border:1px solid var(--line);background:var(--panel);padding:8px 9px;font-size:9px;color:#555;line-height:12px}
.promo h3{color:var(--red);font-size:12px;font-weight:700;line-height:14px;white-space:nowrap}
.promo .sub{color:#555;font-size:9px;margin-bottom:10px}
.promo .pic{position:absolute;right:8px;top:12px;width:52px;height:46px;border-radius:4px}

/* centre */
.intro-title{left:212px;top:172px;font-size:17px;color:#222}
.intro{left:212px;top:200px;width:456px;font-size:10.3px;line-height:15.6px;color:#555}
.tile{width:106px;height:130px;border:4px solid #ddd;background:var(--white);padding:6px}
.tile .ph{width:100%;height:100%;border-radius:2px}
.cap{width:118px;text-align:center;font-size:11px;color:#444;letter-spacing:.3px;line-height:13px}
.dots{left:208px;top:530px;width:461px;border-top:2px dotted #c8c8c8}
.bar{left:208px;top:540px;width:461px;height:30px;background:linear-gradient(#d61614,#a30b0a);color:var(--white);font-size:16px;padding:6px 6px;display:flex;justify-content:space-between}
.bar small{font-size:9px;font-weight:700;padding-top:4px}
.cable{background:radial-gradient(circle at 50% 55%,#e8602a 0,#2e9a5a 22%,#3b7fd0 38%,#e6d23a 52%,#fff 66%)}

/* right column */
.rhead{left:675px;width:159px;background:linear-gradient(#d61614,#a30b0a);color:var(--white);font-size:14px;padding:6px 9px;line-height:17px;white-space:nowrap}
.rbox{left:675px;width:159px;border:1px solid var(--line);background:var(--panel)}
.btn{position:absolute;height:24px;font-size:10px;border-radius:3px;display:flex;align-items:center;justify-content:center}
.mail{position:absolute;left:8px;top:78px;width:141px;height:20px;background:var(--white);border:1px solid #bbb;font-size:9px;color:#555;padding:4px 5px}
.quote{position:absolute;left:8px;top:8px;width:141px;height:88px;background:#e8e8e8;padding:7px 7px 0 34px;font-family:"Tinos",serif;font-style:italic;font-size:10.5px;line-height:12px;color:#444;text-align:right}

/* footer */
.foot-links{left:32px;top:991px;width:810px;height:30px;background:var(--footer);display:flex;justify-content:center;align-items:center;gap:10px;font-size:10px;color:var(--foot-text)}
.foot-links i{color:#777;font-style:normal}
.cols{left:32px;top:1030px;width:810px;height:130px;display:flex}
.col{border-right:1px solid #3a3a3a;padding:2px 9px;font-size:9.8px;line-height:15.5px;color:var(--foot-text);white-space:nowrap}
.col:last-child{border:0}
.col h4{font-size:8.8px;font-weight:700;color:var(--white);margin-bottom:5px}
.bottom{left:0;top:1166px;width:874px;height:34px;background:#0e0e0e;color:#ccc;font-size:10px;text-align:center;padding-top:13px}
.social{top:1174px;width:18px;height:18px;border-radius:3px}
</style>
</head>
<body>
<div class="abs top-rule"></div>

<header>
  <div class="abs brand"><span>Wirovant</span><span class="mark"></span></div>
  <div class="abs search"><div class="field">Search Term</div><div class="go">Search</div></div>
  <div class="abs support-avatar" role="img" aria-label="Support staff avatar"></div>
  <div class="abs support">Need Support?<br>Live Chat</div>
  <div class="abs phone">
    <svg width="13" height="13" viewBox="0 0 24 24" fill="#fff"><path d="M6.6 10.8a15.1 15.1 0 0 0 6.6 6.6l2.2-2.2c.3-.3.7-.4 1-.2 1.1.4 2.3.6 3.6.6.6 0 1 .4 1 1V20c0 .6-.4 1-1 1A17 17 0 0 1 3 4c0-.6.4-1 1-1h3.5c.6 0 1 .4 1 1 0 1.3.2 2.5.6 3.6.1.3 0 .7-.2 1z"/></svg>
    <span>1300 555 019</span>
  </div>
  <div class="abs hours">Mon - Fri ( 9am - 5pm ) AEST</div>
</header>

<main>
  <div class="abs sheet"></div>
  <nav class="abs nav">
    <span>HOME</span><span>ABOUT US</span><span>OUR CATALOGUE</span><span>WHOLESALE OUTLET STORES</span><span>EDUCATION / GOVERNMENT</span><span>SHIPPING</span><span>PAYMENTS</span><span>CONTACT US</span><span class="login">ACCOUNT / LOGIN</span>
  </nav>

  <aside>
    <ul class="abs cats">
      <li>Cables<span class="arr">›</span></li>
      <li>Data Product<span class="arr">›</span></li>
      <li>Server Cabinets<span class="arr">›</span></li>
      <li>Network Cabinets<span class="arr">›</span></li>
      <li>Fiber Products<span class="arr">›</span></li>
      <li>Coax Products<span class="arr">›</span></li>
      <li>Telephone &amp; Voice<span class="arr">›</span></li>
      <li style="border:0">Tools &amp; Switches<span class="arr">›</span></li>
      <li>&amp; Hardware</li>
      <li>AV Wall Plates &amp; Inserts<span class="arr">›</span></li>
      <li>Plasma &amp; LCD Brackets<span class="arr">›</span></li>
      <li>Cable Ducting Conduit<span class="arr">›</span></li>
    </ul>
    <div class="abs promo" style="top:507px;height:101px">
      <h3>SAFE PAYMENT<br>METHODS</h3>
      <div class="pic" style="top:36px;background:linear-gradient(135deg,#dfe6ee,#9fb4cc)" role="img" aria-label="Payment cards"></div>
      <p style="margin-top:14px">KARVO,<br>MERIDA CARD,<br>PAYLON ....</p>
    </div>
    <div class="abs promo" style="top:624px;height:98px">
      <h3>FREE SHIPPING</h3>
      <div class="sub">ON ALL ORDERS</div>
      <div class="pic" style="top:36px;height:44px;background:linear-gradient(135deg,#e9c46a,#8a6a2a)" role="img" aria-label="Forklift carrying boxes"></div>
      <p style="margin-top:28px">DELIVERY DETAILS<br>STOCK AVAILABILITY</p>
    </div>
    <div class="abs promo" style="top:735px;height:97px">
      <h3>100% SAFE</h3>
      <p>SECURE<br>SHOPPING</p>
      <div class="pic" style="border-radius:50%;width:46px;background:radial-gradient(#f7d46a,#c9901a)" role="img" aria-label="Satisfaction guarantee seal"></div>
      <p style="margin-top:14px">WARRANTY<br>QUALITY GUARANTEE</p>
    </div>
  </aside>

  <section>
    <h1 class="abs intro-title" style="font-weight:400">Lorem ipsum dolor sit amet, consectetuer</h1>
    <p class="abs intro">Lorem ipsum dolor sit amet, consectetuer adipiscing elit. Aenean commodo ligula eget dolor. Aenean massa. Cum sociis natoque penatibus et magnis dis parturient montes, nascetur ridiculus mus. Donec quam felis, ultricies nec, pellentesque eu, pretium quis, sem. Nulla consequat massa quis enim. Donec pede justo, fringilla vel, aliquet nec, vulputate eget, arcu. In enim justo, rhoncus ut, imperdiet a, venenatis vitaLorem ipsum dolor sit amet, consectetuer adipiscing elit. Aenean commodo ligula eget dolor. Aenean massa. Cum sociis natoque penatibus et magnis dis parturient montes, nascetur ridiculus mus. Donec quam felis, ultricies nec, Aenean massa. Cum sociis natoque penatibus et magnis dis parturient montes, nascetur ridiculus mus.</p>

    <div class="abs tile" style="left:208px;top:338px"><div class="ph" style="background:linear-gradient(135deg,#fff,#d9d9d9 60%,#fff)" role="img" aria-label="Cables"></div></div>
    <div class="abs tile" style="left:326px;top:338px"><div class="ph" style="background:linear-gradient(160deg,#fff 30%,#444 50%,#fff 70%)" role="img" aria-label="Cable management panel"></div></div>
    <div class="abs tile" style="left:444px;top:338px"><div class="ph" style="background:radial-gradient(circle,#333 30%,#fff 70%)" role="img" aria-label="Data product keystone jack"></div></div>
    <div class="abs tile" style="left:562px;top:338px"><div class="ph" style="background:linear-gradient(#fff 5%,#1c1c1c 10%,#2c2c2c 90%,#fff 95%)" role="img" aria-label="Server rack cabinet"></div></div>
    <div class="abs cap" style="left:202px;top:476px">Cables</div>
    <div class="abs cap" style="left:320px;top:476px">Cable Management</div>
    <div class="abs cap" style="left:438px;top:476px">Data Products</div>
    <div class="abs cap" style="left:556px;top:476px">Server Rack<br>Cabinets</div>

    <div class="abs dots"></div>
    <div class="abs bar"><span>Top Selling Products</span><small>more</small></div>

    <div class="abs tile" style="left:208px;top:584px"><div class="ph cable" role="img" aria-label="Coiled network cables"></div></div>
    <div class="abs tile" style="left:326px;top:584px"><div class="ph cable" role="img" aria-label="Coiled network cables"></div></div>
    <div class="abs tile" style="left:444px;top:584px"><div class="ph cable" role="img" aria-label="Coiled network cables"></div></div>
    <div class="abs tile" style="left:562px;top:584px"><div class="ph cable" role="img" aria-label="Coiled network cables"></div></div>
    <div class="abs cap" style="left:202px;top:725px">Network Cable</div>
    <div class="abs cap" style="left:320px;top:725px">Network Cable</div>
    <div class="abs cap" style="left:438px;top:725px">Network Cable</div>
    <div class="abs cap" style="left:556px;top:725px">Network Cable</div>

    <div class="abs tile" style="left:208px;top:760px"><div class="ph cable" role="img" aria-label="Coiled network cables"></div></div>
    <div class="abs tile" style="left:326px;top:760px"><div class="ph cable" role="img" aria-label="Coiled network cables"></div></div>
    <div class="abs tile" style="left:444px;top:760px"><div class="ph cable" role="img" aria-label="Coiled network cables"></div></div>
    <div class="abs tile" style="left:562px;top:760px"><div class="ph cable" role="img" aria-label="Coiled network cables"></div></div>
    <div class="abs cap" style="left:202px;top:905px">Network Cable</div>
    <div class="abs cap" style="left:320px;top:905px">Network Cable</div>
    <div class="abs cap" style="left:438px;top:905px">Network Cable</div>
    <div class="abs cap" style="left:556px;top:905px">Network Cable</div>
  </section>

  <aside>
    <div class="abs rhead" style="top:164px;height:31px;font-size:15px">SHOPPING CART</div>
    <div class="abs rbox" style="top:195px;height:120px">
      <div class="abs" style="left:12px;top:22px;width:42px;height:34px;border-radius:4px;background:linear-gradient(#f8d24a,#d59a12)" role="img" aria-label="Shopping basket"></div>
      <div class="abs" style="left:72px;top:24px;font-size:10px;line-height:19px;color:#444">Items: 0<br>Total: $0.00</div>
      <div class="btn" style="left:12px;top:88px;width:64px;background:var(--red);color:#fff">View cart</div>
      <div class="btn" style="left:82px;top:88px;width:64px;background:#ddd;color:var(--red)">Checkout</div>
    </div>
    <div class="abs rhead" style="top:331px;height:40px;padding-top:12px">WHY CLIENT?</div>
    <div class="abs" style="left:790px;top:326px;width:38px;height:45px;border-radius:4px;background:linear-gradient(#d8d8d8,#3a3a3a)" role="img" aria-label="Business person"></div>
    <div class="abs rhead" style="top:381px;height:49px;font-size:13.2px;padding:7px 8px">CERTIFICATES &amp;<br>QUALITY ASSURANCE</div>
    <div class="abs rbox" style="top:430px;height:126px;background:#fff">
      <div class="abs" style="left:20px;top:14px;width:120px;height:96px;border:1px solid #ccc;background:linear-gradient(90deg,#e8e8e8 50%,#dde3ee 50%)" role="img" aria-label="Quality certification badge"></div>
    </div>
    <div class="abs rhead" style="top:566px;height:27px">OUR NEWSLETTER</div>
    <div class="abs rbox" style="top:593px;height:145px;background:#fff">
      <div class="abs" style="left:9px;top:8px;font-size:11.5px;color:#444">JOIN OUR NEWSLETTER</div>
      <div class="abs" style="left:9px;top:26px;width:140px;font-size:9.5px;line-height:13px;color:#777">Discover exclusive offers, products previews and much more......</div>
      <div class="mail">Enter your mail</div>
      <div class="btn" style="left:8px;top:105px;width:138px;background:#1c1c1c;color:#fff;font-size:11px;font-weight:700">GET SPECIAL OFFERS</div>
    </div>
    <div class="abs rhead" style="top:748px;height:27px">TESTIMONIALS</div>
    <div class="abs rbox" style="top:775px;height:123px;background:#fff">
      <div class="quote">Lorem ipsum dolor sitmet, consectetuer adipiscing elit. Aenean commodo ligula eget dolor. Aenean massa. Cum sociis nat.</div>
      <div class="abs" style="left:8px;top:8px;font-family:'Tinos',serif;font-size:46px;color:#c8c8c8;line-height:40px">“</div>
      <div class="abs" style="left:40px;top:101px;font-size:10px;color:#444">NAME</div>
      <div class="abs" style="left:104px;top:107px;font-size:10px;color:var(--red)">View more</div>
    </div>
  </aside>
</main>

<footer>
  <div class="abs foot-links">
    <span>Home</span><i>|</i><span>About Wirovant</span><i>|</i><span>My Account</span><i>|</i><span>Order Status</span><i>|</i><span>Wish List</span><i>|</i><span>Gift Certificate</span><i>|</i><span>View Cart</span><i>|</i><span>Sign In</span><i>|</i><span>Create An Account</span>
  </div>
  <div class="abs cols">
    <div class="col" style="width:241px"><h4>SERVER RACKS / NETWORK COMPUTER CABINETS</h4>Network Cabinet &amp; Rack Mount Accesories<br>Wall Mount Network Cabinets<br>Half Height Floor Server Racks<br>Full Height Server Racks<br>Wall Mount Frames<br>Network Cabinet Shelves</div>
    <div class="col" style="width:146px"><h4>CABLE MANAGEMENT</h4>Cable Management Rings<br>Cable Floor Covers<br>Cable Management Rails<br>Cable Ties<br>Cable Tray</div>
    <div class="col" style="width:112px"><h4>ETHERNET CABLES</h4>Cat 5E Cable<br>Cat 6 Cable</div>
    <div class="col" style="width:184px"><h4>FIBRE PRODUCTS</h4>Multimode Fibre Optic Patch Cables<br>Single Mode Fibre Optic Patch Leads<br>Fibre Optic Cable</div>
    <div class="col" style="width:127px"><h4>PATCH PANELS</h4>Cat5e Patch Panel<br>Cat 6 Patch Panels</div>
  </div>
  <div class="abs bottom">Copyright 2011 Wirovant. All rights reserved. Terms and conditions</div>
  <div class="abs social" style="left:752px;background:#3c5a99" role="img" aria-label="Social profile link"></div>
  <div class="abs social" style="left:781px;background:#4aa3df" role="img" aria-label="Social profile link"></div>
</footer>
</body>
</html>
```